Webdesign für K&L Vendora GmbH
Zielgruppe
- Partner für moderne Automaten- und Verpflegungslösungen in Unternehmen
- Zielgruppe sind Unternehmen, welche Versorgungskonzepte schaffen, die optimal auf die Bedürfnisse von Mitarbeitenden, Kunden und Gästen abgestimmt sind
Aufgabenstellung
- KEINE Kopie der alten Webseite
- Farbkonzept gern in sanften Kaffeetönen kombiniert mit Weiß
- Klare Struktur der Webseite

```html
<!DOCTYPE html>
<html lang="de">
<head>
<meta charset="utf-8">
<title>K&amp;L Vendora GmbH – Moderne Automaten für Unternehmen</title>
<link href="https://fonts.googleapis.com/css2?family=Inter:wght@400;500;600;700;800;900&display=swap" rel="stylesheet">
<style>
  :root{
    --navy:#0f1f5c;
    --blue:#6b93cf;
    --ink:#111111;
    --text:#1e1e1e;
    --paper:#ffffff;
    --backdrop:#ffffff;
    --logo-disc:#e9edf5;
  }
  *{margin:0;padding:0;box-sizing:border-box}
  html,body{width:1200px;height:1200px;overflow:hidden;background:var(--backdrop)}
  body{font-family:"Inter",sans-serif;color:var(--text);position:relative}
  .page{position:absolute;left:76px;top:72px;width:1057px;height:1128px;background:var(--paper);box-shadow:0 0 40px rgba(0,0,0,.08);overflow:hidden}
  .abs{position:absolute}

  /* header */
  .brand-disc{left:62px;top:14px;width:60px;height:60px;border-radius:50%;background:var(--logo-disc)}
  .brand-name{left:130px;top:22px;font-weight:800;font-size:24px;color:var(--ink);line-height:1}
  .brand-sub{left:131px;top:49px;font-weight:600;font-size:12px;color:var(--ink);line-height:1}
  .nav a{position:absolute;top:28px;font-weight:700;font-size:15px;color:var(--ink);text-decoration:none;line-height:1}
  .nav a.active{color:var(--navy)}
  .nav a.active::after{content:"";position:absolute;left:0;right:0;bottom:-5px;height:2px;background:var(--blue)}
  .burger{left:1018px;top:30px;width:14px}
  .burger span{display:block;height:2px;background:var(--ink);margin-bottom:3px}
  .contact-pill{left:812px;top:61px;width:245px;height:22px;background:var(--blue);border-radius:11px 0 0 11px;color:#fff;font-size:10.5px;font-weight:600;display:flex;align-items:center;gap:17px;padding-left:14px}

  /* hero */
  .hero{left:0;top:83px;width:1057px;height:513px;background:
    linear-gradient(90deg,rgba(240,238,228,.85) 0%,rgba(235,232,220,.55) 35%,rgba(0,0,0,0) 55%),
    linear-gradient(100deg,#cfd2bf 0%,#b9b99c 25%,#a89a82 45%,#d1b79a 58%,#8a7a68 72%,#4b4741 85%,#2f2e2c 100%)}
  .hero-disc{left:50px;top:155px;width:48px;height:48px;border-radius:50%;background:var(--logo-disc)}
  .hero-title{left:51px;top:219px;font-weight:900;font-size:35px;line-height:39px;color:var(--ink);letter-spacing:-.2px}
  .hero-sub{left:51px;top:301px;font-weight:500;font-size:20px;line-height:24px;color:var(--ink)}
  .hero-copy{left:51px;top:366px;width:330px;font-size:11.6px;line-height:16.6px;color:var(--ink)}
  .cta{left:52px;top:469px;width:131px;height:42px;border-radius:21px;background:var(--navy);color:#fff;font-weight:600;font-size:14px;display:flex;align-items:center;justify-content:center}
  .call-badge{left:366px;top:423px;width:126px;height:126px;border-radius:50%;background:var(--blue);color:#fff;display:flex;flex-direction:column;align-items:center;justify-content:center;text-align:center;transform:rotate(10deg);font-size:13px;line-height:15px}
  .call-badge b{font-weight:800;font-size:12.5px;margin-top:2px}

  /* offer section */
  .offer-circle{left:72px;top:643px;width:400px;height:400px;border-radius:50%;background:var(--blue)}
  .machine{border-radius:3px}
  .machine-snack{left:104px;top:670px;width:171px;height:329px;background:linear-gradient(180deg,#1b1d22 0%,#3a2f2a 45%,#1b1d22 75%,#b9bcc1 100%)}
  .machine-coffee{left:297px;top:702px;width:137px;height:366px;background:linear-gradient(180deg,#2a1e17 0%,#4b3325 25%,#1b1b1d 45%,#2a2b2e 70%,#4b3325 85%,#2a1e17 100%)}
  .offer-title{left:544px;top:675px;font-weight:800;font-size:33px;line-height:38px;color:var(--navy);letter-spacing:-.3px}
  .offer-rule{left:545px;top:757px;width:35px;height:3px;background:var(--blue)}
  .offer-copy{left:544px;top:793px;font-size:13.6px;line-height:20px;color:var(--ink)}
  .offer-lead{left:544px;top:894px;font-weight:700;font-size:13.6px;color:var(--ink)}
  .offer-list{left:544px;top:934px;list-style:none;font-size:13.6px;line-height:21.9px;color:var(--ink)}
  .offer-list li{display:flex;align-items:center;gap:8px}
  .offer-list svg{flex:none}
</style>
</head>
<body>
<div class="page">
  <header>
    <div class="abs brand-disc"></div>
    <div class="abs brand-name">K&amp;L Vendora</div>
    <div class="abs brand-sub">GmbH</div>
    <nav class="nav">
      <a class="active" href="#" style="left:453px">Home</a>
      <a href="#" style="left:567px">Produkte</a>
      <a href="#" style="left:693px">Über Uns</a>
      <a href="#" style="left:828px">Kontakt</a>
    </nav>
    <div class="abs burger"><span></span><span></span><span></span></div>
    <div class="abs contact-pill"><span>+49 371 555 0147</span><span>info@kl-vendora.de</span></div>
  </header>

  <section class="abs hero" role="img" aria-label="Foto: lächelnde Frau bedient einen Snackautomaten im Freien">
    <div class="abs hero-disc"></div>
    <h1 class="abs hero-title">MODERNE AUTOMATEN<br>FÜR UNTERNEHMEN</h1>
    <p class="abs hero-sub">Kaffee, Getränke und Snacks<br>mit Rundum-Service</p>
    <p class="abs hero-copy">Wir treffen mit Ihnen eine bedarfsgerechte Auswahl an Heißgetränkeautomaten, Kaltgetränkeautomaten, Snack- und Speiseautomaten, sowie für Wasserspender in verschiednen Varianten.</p>
    <div class="abs cta">Mehr erfahren</div>
    <div class="abs call-badge"><span>Rufen Sie uns<br>an unter:</span><b>+49 371 555 0147</b></div>
  </section>

  <section>
    <div class="abs offer-circle"></div>
    <div class="abs machine machine-snack" role="img" aria-label="Produktfoto: Snackautomat mit Glasfront"></div>
    <div class="abs machine machine-coffee" role="img" aria-label="Produktfoto: Heißgetränkeautomat mit Kaffeebohnen-Motiv"></div>
    <h2 class="abs offer-title">Maßgeschneiderte<br>Versorgungskonzepte</h2>
    <div class="abs offer-rule"></div>
    <p class="abs offer-copy">Jedes Unternehmen hat unterschiedliche Bedürfnisse.<br>Deshalb beraten wir Sie persönlich und entwickeln gemeinsam<br>mit Ihnen die optimale Lösung für Ihren Standort.</p>
    <p class="abs offer-lead">Unser Angebot umfasst:</p>
    <ul class="abs offer-list">
      <li><svg width="8" height="8" viewBox="0 0 8 8"><path d="M1 4.2 3 6.4 7 1.5" fill="none" stroke="#6b93cf" stroke-width="1.6"/></svg>Heißgetränkeautomaten für Kaffee, Cappuccino,</li>
      <li><svg width="8" height="8" viewBox="0 0 8 8"><path d="M1 4.2 3 6.4 7 1.5" fill="none" stroke="#6b93cf" stroke-width="1.6"/></svg>Kakao und weitere Spezialitäten</li>
      <li><svg width="8" height="8" viewBox="0 0 8 8"><path d="M1 4.2 3 6.4 7 1.5" fill="none" stroke="#6b93cf" stroke-width="1.6"/></svg>Kaltgetränkeautomaten für Erfrischungsgetränke und Wasser</li>
      <li><svg width="8" height="8" viewBox="0 0 8 8"><path d="M1 4.2 3 6.4 7 1.5" fill="none" stroke="#6b93cf" stroke-width="1.6"/></svg>Snack- und Speiseautomaten für die Verpflegung rund um die Uhr</li>
      <li><svg width="8" height="8" viewBox="0 0 8 8"><path d="M1 4.2 3 6.4 7 1.5" fill="none" stroke="#6b93cf" stroke-width="1.6"/></svg>Wasserspender für Büros, Produktionsstätten und Empfangsbereiche</li>
      <li><svg width="8" height="8" viewBox="0 0 8 8"><path d="M1 4.2 3 6.4 7 1.5" fill="none" stroke="#6b93cf" stroke-width="1.6"/></svg>Moderne Bezahlsysteme und individuelle Ausstattungsoptionen</li>
    </ul>
  </section>
</div>
</body>
</html>
```